I need a simple, classy and stylish business card. I would like it to have a black background with white writing. I would like you to use my logo you designed on the front with the word 'Imagery" used underneath it in the same font. On the back I was thinking of the website at the top 'tomverrick.com' Then my social media accounts, Can you use the instagram, Facebook and twitter logo then my handles?
Please let me know what you think.
Regards Tom
Must have
- Website: www.tomverrick.com
- Social media handles..
- Instagram: @Tom_Verrick_Imagery
- Facebook: Tom Verrick Imagery
- Twitter: @Tom_Verrick
- Email: info@tomverick.com
- Phone: 0437 518 293

```html
<!DOCTYPE html>
<html lang="en">
<head>
<meta charset="utf-8">
<title>Tom Verrick Imagery — Business Card</title>
<link rel="stylesheet" href="https://fonts.googleapis.com/css2?family=Open+Sans:wght@300;400&display=swap">
<style>
  :root {
    --stage: #e9e9ea;
    --card-front: #0b0b0b;
    --card-back: #1f1c1c;
    --ink: #ffffff;
    --ink-soft: #d9d9d9;
    --rule: #bdbdbd;
    --mark-short: #4fa6cc;
    --mark-page: #4a68a8;
    --mark-photo: #9a8672;
  }
  * { margin: 0; padding: 0; box-sizing: border-box; }
  html, body {
    width: 1200px; height: 1200px; overflow: hidden;
    background: var(--stage);
    font-family: "Open Sans", sans-serif;
  }
  .stage {
    width: 1200px; height: 1200px;
    display: flex; flex-direction: column;
    align-items: center; justify-content: center; gap: 90px;
  }
  .card {
    width: 770px; height: 440px;
    border-radius: 4px;
    box-shadow: 0 14px 30px rgba(0,0,0,0.22);
    color: var(--ink);
    position: relative;
  }
  .card--front {
    background: var(--card-front);
    display: flex; align-items: center; justify-content: center;
  }
  .brand { display: flex; flex-direction: column; align-items: center; }
  .brand__name {
    display: flex; align-items: center; gap: 22px;
    font-weight: 300; font-size: 64px; letter-spacing: 1px;
  }
  .brand__dot {
    width: 22px; height: 22px; border-radius: 50%;
    background: var(--ink);
  }
  .brand__tag {
    margin-top: 6px; margin-left: 44px;
    font-weight: 300; font-size: 26px;
    letter-spacing: 22px; color: var(--ink-soft);
  }
  .card--back {
    background: var(--card-back);
    display: flex; align-items: center; justify-content: center; gap: 30px;
  }
  .contact {
    text-align: right; font-size: 19px; line-height: 1.75;
    color: var(--ink-soft); letter-spacing: 0.3px;
  }
  .divider { width: 1px; height: 120px; background: var(--rule); }
  .socials { list-style: none; font-size: 19px; line-height: 1.75; color: var(--ink-soft); }
  .socials li { display: flex; align-items: center; gap: 10px; }
  .socials__mark { width: 15px; height: 15px; border-radius: 2px; flex: none; }
  .socials__mark--short { background: var(--mark-short); }
  .socials__mark--page { background: var(--mark-page); }
  .socials__mark--photo { background: var(--mark-photo); }
</style>
</head>
<body>
<main class="stage">
  <section class="card card--front" aria-label="Card front">
    <div class="brand">
      <div class="brand__name"><span class="brand__dot"></span>Tom Verrick</div>
      <div class="brand__tag">Imagery</div>
    </div>
  </section>
  <section class="card card--back" aria-label="Card back">
    <div class="contact">
      <p>T. 0437 518 293</p>
      <p>W. www.tomverrick.com</p>
      <p>E. info@tomverick.com</p>
    </div>
    <span class="divider"></span>
    <ul class="socials">
      <li><span class="socials__mark socials__mark--short"></span>@Tom_Verrick</li>
      <li><span class="socials__mark socials__mark--page"></span>@TomVerrickImagery</li>
      <li><span class="socials__mark socials__mark--photo"></span>@Tom_Verrick_Imagery</li>
    </ul>
  </section>
</main>
</body>
</html>
```